All Natural Raw Honey & Goats Milk Body Wash Labels

We have launched a new product line of all natural Raw Honey & Goats Milk body wash with the business name being Vale Orin and the tag line Kindred . Their are currently three line items requiring three labels. Natural (Unscented), Japanese Honeysuckle and Caribbean.
It is a family orientated product that we want to promote as being all natural, healthy and trustworthy. It is an all Australian made product that uses our very own award winning raw honey
I can supply the file for the business name/logo upon request

Families

Bath & body

• a Lux high end feel
• simple easy to read with minimal images
• No cartoons

```html
<!DOCTYPE html>
<html lang="en">
<head>
<meta charset="utf-8">
<title>Vale Orin — Raw Honey &amp; Goats Milk Body Wash Labels</title>
<link href="https://fonts.googleapis.com/css2?family=Jost:wght@400;500&family=Oswald:wght@500&display=swap" rel="stylesheet">
<style>
  :root {
    --bg: #d9dbe0;
    --ink: #ffffff;
    --carib-marble-a: #86c1cb;
    --carib-marble-b: #6aa8b4;
    --carib-band: #4e8a98;
    --carib-strip: #8fc6cf;
    --natural-marble-a: #5a8a72;
    --natural-marble-b: #41705a;
    --natural-band: #86d2ab;
    --honey-marble-a: #b0623f;
    --honey-marble-b: #8c4630;
    --honey-band: #f3893a;
  }
  * { margin: 0; padding: 0; box-sizing: border-box; }
  html, body { width: 1200px; height: 900px; overflow: hidden; }
  body {
    background: linear-gradient(135deg, #e6e7eb 0%, var(--bg) 100%);
    font-family: "Jost", sans-serif;
    color: var(--ink);
  }
  .label-set {
    position: absolute;
    top: 200px;
    left: 60px;
    display: flex;
    gap: 30px;
  }
  .label {
    position: relative;
    width: 340px;
    height: 500px;
    overflow: hidden;
    text-align: center;
  }
  .label__marble {
    position: absolute;
    inset: 0;
  }
  .label__strip {
    position: absolute;
    left: 0; right: 0; top: 0;
    height: 26px;
  }
  .label__content {
    position: relative;
    padding-top: 62px;
  }
  .label__formula {
    font-size: 24px;
    font-weight: 500;
    letter-spacing: 0.2px;
  }
  .label__type {
    margin-top: 10px;
    font-size: 24px;
    font-weight: 500;
    letter-spacing: 1px;
  }
  .brand {
    margin-top: 64px;
    display: flex;
    flex-direction: column;
    align-items: center;
  }
  .brand__name {
    display: flex;
    align-items: center;
    gap: 12px;
    font-size: 40px;
    font-weight: 400;
  }
  .brand__dot {
    width: 12px; height: 12px;
    border-radius: 50%;
    background: var(--ink);
  }
  .brand__tagline {
    margin-top: 8px;
    font-size: 14px;
    font-weight: 500;
    letter-spacing: 7px;
    text-transform: uppercase;
  }
  .label__variant {
    position: absolute;
    left: 0; right: 0;
    bottom: 60px;
    height: 66px;
    display: flex;
    align-items: center;
    justify-content: center;
    font-family: "Oswald", sans-serif;
    font-size: 21px;
    font-weight: 500;
    letter-spacing: 0.5px;
    text-transform: uppercase;
  }

  .label--caribbean .label__marble {
    background: linear-gradient(160deg, var(--carib-marble-a) 0%, var(--carib-marble-b) 50%, var(--carib-marble-a) 100%);
  }
  .label--caribbean .label__strip { background: var(--carib-strip); }
  .label--caribbean .label__variant { background: var(--carib-band); }

  .label--natural .label__marble {
    background: linear-gradient(160deg, var(--natural-marble-a) 0%, var(--natural-marble-b) 50%, var(--natural-marble-a) 100%);
  }
  .label--natural .label__strip { background: var(--natural-band); }
  .label--natural .label__variant { background: var(--natural-band); }

  .label--honeysuckle .label__marble {
    background: linear-gradient(160deg, var(--honey-marble-a) 0%, var(--honey-marble-b) 50%, var(--honey-marble-a) 100%);
  }
  .label--honeysuckle .label__strip { background: var(--honey-band); }
  .label--honeysuckle .label__variant { background: var(--honey-band); }
</style>
</head>
<body>
  <main class="label-set">
    <section class="label label--caribbean">
      <div class="label__marble" role="img" aria-label="Soft teal marbled swirl pattern"></div>
      <div class="label__strip"></div>
      <div class="label__content">
        <p class="label__formula">Raw Honey &amp; Goats Milk</p>
        <p class="label__type">BODY WASH</p>
        <div class="brand">
          <p class="brand__name"><span class="brand__dot"></span>Vale Orin</p>
          <p class="brand__tagline">Kindred .</p>
        </div>
      </div>
      <p class="label__variant">Caribbean</p>
    </section>

    <section class="label label--natural">
      <div class="label__marble" role="img" aria-label="Deep green marbled swirl pattern"></div>
      <div class="label__strip"></div>
      <div class="label__content">
        <p class="label__formula">Raw Honey &amp; Goats Milk</p>
        <p class="label__type">BODY WASH</p>
        <div class="brand">
          <p class="brand__name"><span class="brand__dot"></span>Vale Orin</p>
          <p class="brand__tagline">Kindred .</p>
        </div>
      </div>
      <p class="label__variant">Natural (Unscented)</p>
    </section>

    <section class="label label--honeysuckle">
      <div class="label__marble" role="img" aria-label="Rust orange marbled swirl pattern"></div>
      <div class="label__strip"></div>
      <div class="label__content">
        <p class="label__formula">Raw Honey &amp; Goats Milk</p>
        <p class="label__type">BODY WASH</p>
        <div class="brand">
          <p class="brand__name"><span class="brand__dot"></span>Vale Orin</p>
          <p class="brand__tagline">Kindred .</p>
        </div>
      </div>
      <p class="label__variant">Japanese Honey Suckle</p>
    </section>
  </main>
</body>
</html>
```